Cooler Trailer Rental Flyer

I need a flyer designed to showcase a rental product.

We own two refrigerated Cooler Trailers. One trailer is 7’ x 12’. The second trailer is 7’ x 16’. Each unit is a double axle trailer with a cargo capacity of 8000 lbs. The refrigeration unit is 110v and is capable of cooling or freezing with just 12 amps. The 12’ unit comes with a securely mounted generator for stand-alone service needs, and we have a portable generator available if needed for the 16’ unit.

The trailer requires a class III or class IV hitch, with a 2 5/16” ball for towing and a 7-pin two vehicle socket for the trailer wiring.

We offer delivery for $1.40 per loaded mile (we only charge for the miles with the trailer attached, so one way for delivery or pickup). This option may make sense for many reasons, including:
- saving the cost of your time
- saving the cost of fuel
- eliminating your liability for the trailer while towing
- preventing you from having to buy any towing equipment

Our farm is located at 4127 Halvern Mills Avenue, Halvern Mills, Michigan 48672. The name of the farm/business is Maple Hollow Farm.

The rental rates are as follows:
$169/day (two day minimum rental required)
$599/week
$1500/month

A $100 deposit is required to reserve the trailer. The deposit is fully refundable up to two weeks prior to the event, 50% up to one week, and non-refundable within one week of the event.

The website for the place we bought the trailer is www.frostvanhaul.example. A link to a video from his website is https://frostvanhaul.example/refrigerated-trailer-videos/

I would like the flyer to be colorful and professional, with photos.
Updates

Several notes: 1. I have added the logo for Maple Hollow Farm. 2. Contact information for the brochure should be as follows: Martin or Colleen Verlander Maple Hollow Farm 5816 Maple Hollow Drive SW Halvern Mills, MI 48672 (616) 555-0147 3. Please note that we are not "FrostVanHaul.example". This is the website for the manufacturer of the trailers.

Here are some rental ideas that might be worth including: Emergencies and Power Outages Food Distributors Food Vendors Restaurants Caterers Ice Vendors Pubs and Microbreweries Resorts Festivals Open Markets Sporting Events Parties Weddings Floral Distributors Meat Processors Hunters

e-mail address is maplehollowfarm@mailbox.example

Target Market(s)

Food distributors, caterers, resorts, events (festivals, weddings, fairs, parades, parties, concerts), restaurants, breweries, farmers markets, vending companies, big game hunters

Font styles to use
Serif
Sans Serif

Colors

Designer to choose colors to be used in the design.

Requirements
Nice to have
• Tri-fold flyer

```html
<!DOCTYPE html>
<html lang="en">
<head>
<meta charset="utf-8">
<title>Cooler Trailer Rental – Maple Hollow Farm</title>
<link href="https://fonts.googleapis.com/css2?family=Lato:wght@400;700;900&display=swap" rel="stylesheet">
<style>
  :root{
    --navy:#1b2a84;
    --navy-deep:#16226e;
    --yellow:#f5e81c;
    --red:#c8202a;
    --paper:#ffffff;
    --paper-soft:#f3f4f8;
    --ink:#1b2a84;
    --strip:#3a3a3c;
    --backdrop:#8c8c8c;
    --photo-sky:#c9d6e4;
    --photo-ground:#d9d2c2;
  }
  *{box-sizing:border-box;margin:0;padding:0}
  html,body{width:800px;height:1200px;overflow:hidden}
  body{background:var(--backdrop);font-family:'Lato',sans-serif;position:relative}
  .sheet{position:absolute;left:62px;width:678px;height:480px;background:var(--paper);display:flex;box-shadow:0 6px 18px rgba(0,0,0,.3)}
  .sheet--outside{top:78px}
  .sheet--inside{top:636px}
  .panel{position:relative;width:226px;height:100%;overflow:hidden}
  .photo{position:absolute;background:linear-gradient(180deg,var(--photo-sky) 0%,#e9eef3 45%,#f4f4f2 60%,var(--photo-ground) 100%)}
  .strip{position:absolute;left:0;right:0;bottom:0;height:16px;background:linear-gradient(180deg,#555 0%,var(--strip) 100%)}
  .navy{background:var(--navy)}

  /* outside */
  .blurb{position:absolute;left:16px;right:16px;top:397px;font-size:9.6px;line-height:12px;color:var(--ink);font-weight:700;text-align:justify}
  .contacts{position:absolute;inset:0 0 125px 0;color:#fff;text-align:center;font-size:9.6px;line-height:12px}
  .contact{position:absolute;left:0;right:0}
  .contact svg{display:block;margin:0 auto 7px}
  .social{position:absolute;top:400px;left:0;right:0;display:flex;justify-content:center;gap:9px}
  .social span{width:27px;height:27px;border:1.5px solid var(--navy);border-radius:50%}
  .brand{position:absolute;top:0;left:0;right:0;height:224px;display:flex;flex-direction:column;align-items:center;justify-content:center;gap:10px}
  .brand-mark{width:14px;height:14px;border-radius:50%;background:var(--red)}
  .brand-name{color:var(--red);font-weight:700;font-size:20px;letter-spacing:1px;text-align:center;line-height:24px}
  .cover-title{position:absolute;top:355px;left:0;right:0;height:109px;display:flex;align-items:center;justify-content:center;text-align:center;color:#fff;font-weight:900;font-size:29px;line-height:32px}

  /* inside */
  .panel--about{background:var(--paper-soft)}
  .about-head{position:absolute;left:16px;top:20px;font-size:11.5px;font-weight:700;color:var(--ink);border-bottom:2px solid #3d8fd9;padding-bottom:1px}
  .about-text{position:absolute;left:16px;right:16px;top:44px;font-size:9px;line-height:11.6px;color:#222;text-align:justify}
  .hitch{position:absolute;left:16px;right:16px;top:391px;font-size:11px;line-height:13.6px;font-weight:700;color:var(--ink)}
  .offer{position:absolute;left:16px;right:14px;color:#fff;font-size:9.4px;line-height:12px}
  .offer .hl{color:var(--yellow);font-weight:700}
  .offer-lead{color:var(--yellow)}
  .ticks{list-style:none}
  .ticks li{position:relative;padding-left:12px;margin-bottom:8px}
  .ticks li::before{content:"✓";position:absolute;left:0;top:0}
  .ticks--yellow li::before{color:var(--yellow)}
  .rates-head{position:absolute;left:16px;top:216px;color:var(--yellow);font-size:11.5px;font-weight:700;border-bottom:1px solid var(--yellow)}
  .rates li{margin-bottom:6px}
  .rates small{font-size:7.6px;color:#fff;font-weight:400}
  .deposit-band{position:absolute;left:0;right:0;top:320px;height:13px;background:var(--yellow);color:var(--navy-deep);font-size:8.4px;font-weight:700;text-align:center;line-height:13px}
  .gallery-title{position:absolute;left:29px;top:22px;width:168px;height:18px;background:var(--navy);color:#fff;font-size:12px;text-align:center;line-height:18px}
  .gallery-photo{left:42px;width:143px;height:90px;border:2px solid var(--navy)}
  .gallery-photo--interior{background:linear-gradient(180deg,#e6e9ee,#fbfbfc 60%,#d8dbe0)}
</style>
</head>
<body>

<section class="sheet sheet--outside">
  <div class="panel">
    <div class="photo" style="left:0;top:0;width:226px;height:355px" role="img" aria-label="Row of white refrigerated cooler trailers parked on sandy ground under a cloudy sky"></div>
    <p class="blurb">Our farm offers fresh produce and flowers, as well as hanging plants and pumpkins! During season, please stop by our roadside stand at 4127 Halvern Mills Avenue!</p>
    <div class="strip"></div>
  </div>

  <div class="panel">
    <div class="contacts navy">
      <div class="contact" style="top:108px">
        <svg width="12" height="14" viewBox="0 0 12 14" fill="none" stroke="#fff" stroke-width="1.2"><path d="M6 13S1.5 8 1.5 5a4.5 4.5 0 0 1 9 0C10.5 8 6 13 6 13z"/><circle cx="6" cy="5" r="1.6"/></svg>
        4127 Halvern Mills Avenue<br>Halvern Mills, MI 48672
      </div>
      <div class="contact" style="top:193px">
        <svg width="13" height="13" viewBox="0 0 13 13" fill="none" stroke="#fff" stroke-width="1.2"><circle cx="6.5" cy="6.5" r="5.7"/><path d="M4.3 3.6l1.2 1.5-.7.9a4 4 0 0 0 2 2l.9-.7 1.5 1.2-.8 1a5 5 0 0 1-5.1-5.1z"/></svg>
        (616) 555-0147
      </div>
      <div class="contact" style="top:243px">
        <svg width="13" height="10" viewBox="0 0 13 10" fill="none" stroke="#fff" stroke-width="1.2"><rect x=".6" y=".6" width="11.8" height="8.8"/><path d="M.6.6l5.9 5 5.9-5"/></svg>
        maplehollowfarm@mailbox.example
      </div>
      <div class="contact" style="top:293px">
        <svg width="13" height="13" viewBox="0 0 13 13" fill="none" stroke="#fff" stroke-width="1.1"><circle cx="6.5" cy="6.5" r="5.8"/><ellipse cx="6.5" cy="6.5" rx="2.6" ry="5.8"/><path d="M.7 6.5h11.6M1.6 3.5h9.8M1.6 9.5h9.8"/></svg>
        www.maplehollowfarm.example
      </div>
    </div>
    <div class="social" aria-label="Social media links"><span></span><span></span><span></span><span></span></div>
    <div class="strip"></div>
  </div>

  <div class="panel">
    <div class="brand">
      <span class="brand-mark"></span>
      <p class="brand-name">Maple Hollow<br>Farm</p>
    </div>
    <div class="photo" style="left:0;top:224px;width:226px;height:131px" role="img" aria-label="White double axle cooler trailer with a pickup truck beside it"></div>
    <h1 class="cover-title navy">Cooler Trailer<br>Rental</h1>
    <div class="strip"></div>
  </div>
</section>

<section class="sheet sheet--inside">
  <div class="panel panel--about">
    <h2 class="about-head">About</h2>
    <p class="about-text">We have two refrigerated Cooler Trailer models available. One trailer is 7’ x 12’. The second trailer is 7’ x 16’. Each unit is a double axle trailer with a cargo capacity of 8000 lbs. The refrigeration unit is 110v and is capable of cooling or freezing with just 12 amps. The 12’ unit comes with a securely mounted generator for stand-alone service needs, and we have a portable generator available if needed for the 16’ unit.</p>
    <div class="photo" style="left:0;top:196px;width:226px;height:160px" role="img" aria-label="Cooler trailer hitched to a pickup truck on a gravel lot"></div>
    <p class="hitch">The trailer requires a class III or class IV hitch, with a 2 5/16” ball for towing and a 7-pin two vehicle socket for the trailer wiring.</p>
  </div>

  <div class="panel navy">
    <p class="offer hl" style="top:24px">We offer delivery for $1.40 per loaded mile.</p>
    <p class="offer offer-lead" style="top:53px">This option may make sense for<br>many reasons, including:</p>
    <ul class="offer ticks" style="top:80px">
      <li>Saving the cost of your time</li>
      <li>Saving the cost of fuel</li>
      <li>Eliminating your liability for the<br>trailer while towing</li>
      <li>Preventing you from having to buy<br>any towing equipment</li>
    </ul>
    <h2 class="rates-head">The rental rates are as follows:</h2>
    <ul class="offer ticks rates" style="top:244px">
      <li><span class="hl">$169/day</span> <small>(two day minimum rental required)</small></li>
      <li><span class="hl">$599/week</span></li>
      <li><span class="hl">$1500/month</span></li>
    </ul>
    <p class="deposit-band">A $100 deposit is required to reserve the trailer.</p>
    <ul class="offer ticks ticks--yellow" style="top:354px">
      <li style="margin-bottom:14px">The deposit is 100% refundable up to<br>two weeks prior to the rental period.</li>
      <li style="margin-bottom:14px">The deposit is 50% refundable up to<br>one week prior to the rental period.</li>
      <li>The deposit is non-refundable within<br>one week of the rental period.</li>
    </ul>
  </div>

  <div class="panel panel--about">
    <h2 class="gallery-title">Cooler Trailer Rental</h2>
    <div class="photo gallery-photo" style="top:56px" role="img" aria-label="Three cooler trailers lined up"></div>
    <div class="photo gallery-photo" style="top:160px" role="img" aria-label="Rear doors of a cooler trailer"></div>
    <div class="photo gallery-photo" style="top:264px" role="img" aria-label="Side view of a cooler trailer"></div>
    <div class="photo gallery-photo gallery-photo--interior" style="top:368px" role="img" aria-label="White insulated interior of a cooler trailer"></div>
  </div>
</section>

</body>
</html>
```